Android application design for shared calendar app

I need an Android app design for shared calendar, It should have a business look&feel,flat material design. Main part of UI are big clock-like wheels which represent free time and busy time. Busy is red ,free is green. App should have business look & feel but it should be still usable for non business users.

app can be seen here,please try it before starting design
https://apps.quellmarket.net/details?id=com.tidlomo&hl=en

here is a video: https://clipvane.example/v/Rk8pZq2LmTx

Target Market(s)

busy business professionals

Industry/Entity Type

Business

Font styles to use
Sans Serif

Requirements
Must have
• 1) project must have big clock-like circles in which free time is marked in green, busy time in red. so those colors must be green and red but you can use which shades.
• 2) project must have one 16:9 ratio image which has text : click here to load picture which describes your event. and under that text several pictures - business meeting, phone call,some people playing sports,some people in pub. I have attached how it currently look - don't use it, thats just a example :)
• 3) must have default placeholder for user image. I also attached how it currently looks
• 4) buttons and dialogs must be rounded - see how it looks in the app
• 5) events must have semi transparent overlay - see how it looks in the app. font for location and event name can be changed
• 6) App must use eurofurencebold regular for title in action bar., that can't be changed. App must use existing logo (green overlapping clocks)
Nice to have
• a loading page with progress bar should have some interesting picture (city for example)

```html
<!DOCTYPE html>
<html lang="en">
<head>
<meta charset="utf-8">
<title>Tidlomo – Today</title>
<link rel="stylesheet" href="https://fonts.googleapis.com/css2?family=Comfortaa:wght@500&family=Jost:wght@300;400&display=swap">
<style>
  :root {
    --backdrop: #5f7c8a;
    --status-bar: #262626;
    --app-bar: #333333;
    --surface: #ffffff;
    --on-dark: #ffffff;
    --on-dark-muted: #e6e6e6;
    --free: #2ecc40;
    --free-text: #1fb61f;
    --busy: #e0303c;
    --busy-text: #d92834;
    --period-label: #555555;
  }
  * { box-sizing: border-box; margin: 0; padding: 0; }
  html, body {
    width: 1200px; height: 1200px; overflow: hidden;
    background: var(--backdrop);
  }
  .screen {
    position: absolute; left: 271px; top: 16px;
    width: 657px; height: 1167px;
    background: var(--surface);
    display: flex; flex-direction: column;
  }
  .status-bar {
    height: 42px; background: var(--status-bar);
    display: flex; align-items: center; justify-content: flex-end;
    gap: 14px; padding-right: 12px;
    color: var(--on-dark);
    font: 400 22px 'Jost', sans-serif;
  }
  .status-bar svg { display: block; }
  .app-bar {
    height: 189px; background: var(--app-bar);
    display: flex; flex-direction: column;
  }
  .toolbar {
    height: 105px; display: flex; align-items: center;
    justify-content: space-between; padding: 0 34px;
  }
  .app-title {
    color: var(--on-dark);
    font: 500 28px 'Comfortaa', sans-serif;
    letter-spacing: 0.5px;
  }
  .tabs { flex: 1; display: flex; }
  .tab {
    flex: 1; display: flex; align-items: center; justify-content: center;
    color: var(--on-dark-muted);
    font: 400 21px 'Jost', sans-serif;
    text-transform: uppercase;
    border-bottom: 3px solid transparent;
  }
  .tab.is-active { color: var(--on-dark); border-bottom-color: var(--on-dark-muted); }
  .day-wheels { flex: 1; display: block; }
  .hour-label { font: 300 32px 'Jost', sans-serif; }
  .hour-label.free { fill: var(--free-text); }
  .hour-label.busy { fill: var(--busy-text); }
  .period-label { font: 400 72px 'Jost', sans-serif; fill: var(--period-label); }
  .ring-free { fill: none; stroke: var(--free); stroke-width: 5; }
  .ring-busy { fill: none; stroke: var(--busy); stroke-width: 5; }
  .hour-tick { stroke: var(--surface); stroke-width: 2; }
</style>
</head>
<body>
<main class="screen">
  <div class="status-bar">
    <svg width="22" height="18" viewBox="0 0 22 18" aria-hidden="true"><path d="M0 3 Q11 -4 22 3 L11 18 Z" fill="#fff"/></svg>
    <svg width="20" height="18" viewBox="0 0 20 18" aria-hidden="true"><path d="M20 0 V18 H0 Z" fill="#777"/><path d="M12 8 V18 H2 Z" fill="#fff"/></svg>
    <svg width="12" height="20" viewBox="0 0 12 20" aria-hidden="true"><rect x="3" y="0" width="6" height="3" fill="#fff"/><rect x="0" y="3" width="12" height="17" fill="#777"/><rect x="0" y="8" width="12" height="12" fill="#fff"/></svg>
    <span class="status-time">12:30</span>
  </div>

  <header class="app-bar">
    <div class="toolbar">
      <span class="app-title">Tidlomo</span>
      <svg width="8" height="30" viewBox="0 0 8 30" aria-label="More options"><circle cx="4" cy="4" r="3.5" fill="#fff"/><circle cx="4" cy="15" r="3.5" fill="#fff"/><circle cx="4" cy="26" r="3.5" fill="#fff"/></svg>
    </div>
    <nav class="tabs">
      <span class="tab is-active">Today</span>
      <span class="tab">Tomorrow</span>
      <span class="tab">Wednesday</span>
    </nav>
  </header>

  <svg class="day-wheels" width="657" height="936" viewBox="0 0 657 936">
    <defs>
      <g id="hour-wheel">
        <circle class="ring-free" cx="329" cy="254" r="178"/>
        <path class="ring-busy" d="M418 408.1 A178 178 0 0 1 329 432"/>
        <path class="ring-busy" d="M240 408.1 A178 178 0 0 1 151 254"/>
        <g class="hour-ticks">
          <line class="hour-tick" x1="329" y1="71" x2="329" y2="81"/>
          <line class="hour-tick" x1="329" y1="71" x2="329" y2="81" transform="rotate(30 329 254)"/>
          <line class="hour-tick" x1="329" y1="71" x2="329" y2="81" transform="rotate(60 329 254)"/>
          <line class="hour-tick" x1="329" y1="71" x2="329" y2="81" transform="rotate(90 329 254)"/>
          <line class="hour-tick" x1="329" y1="71" x2="329" y2="81" transform="rotate(120 329 254)"/>
          <line class="hour-tick" x1="329" y1="71" x2="329" y2="81" transform="rotate(150 329 254)"/>
          <line class="hour-tick" x1="329" y1="71" x2="329" y2="81" transform="rotate(180 329 254)"/>
          <line class="hour-tick" x1="329" y1="71" x2="329" y2="81" transform="rotate(210 329 254)"/>
          <line class="hour-tick" x1="329" y1="71" x2="329" y2="81" transform="rotate(240 329 254)"/>
          <line class="hour-tick" x1="329" y1="71" x2="329" y2="81" transform="rotate(270 329 254)"/>
          <line class="hour-tick" x1="329" y1="71" x2="329" y2="81" transform="rotate(300 329 254)"/>
          <line class="hour-tick" x1="329" y1="71" x2="329" y2="81" transform="rotate(330 329 254)"/>
        </g>
        <g text-anchor="middle" dominant-baseline="central">
          <text class="hour-label free" x="277" y="61">12</text>
          <text class="hour-label free" x="381" y="61">1</text>
          <text class="hour-label free" x="470" y="113">2</text>
          <text class="hour-label free" x="522" y="202">3</text>
          <text class="hour-label free" x="522" y="306">4</text>
          <text class="hour-label free" x="470" y="395">5</text>
          <text class="hour-label busy" x="381" y="447">6</text>
          <text class="hour-label free" x="277" y="447">7</text>
          <text class="hour-label busy" x="188" y="395">8</text>
          <text class="hour-label busy" x="136" y="306">9</text>
          <text class="hour-label free" x="136" y="202">10</text>
          <text class="hour-label free" x="188" y="113">11</text>
        </g>
      </g>
    </defs>

    <g class="wheel wheel-am">
      <use href="#hour-wheel"/>
      <text class="period-label" x="329" y="254" text-anchor="middle" dominant-baseline="central">AM</text>
    </g>
    <g class="wheel wheel-pm" transform="translate(0 454)">
      <use href="#hour-wheel"/>
      <text class="period-label" x="329" y="254" text-anchor="middle" dominant-baseline="central">PM</text>
    </g>
  </svg>
</main>
</body>
</html>
```